Fashion Label Startup Business Card Design

Maribel Quint is a startup fashion designer based on the Gold Coast in QLD Australia. Maribels label " Vorine by Quint " is based upon taking old world design techniques and infusing them modern twist. The card design should incorporate an old world theme using colours like mustard, ocha, black, white and elements of lace pattern.

Card Details:

Maribel Quint
Fashion Designer
P: 04 0152 6847
E: vorinebyquint@mailbrook.com
W: www.friendsnet.com/VOrineByQuint

```html
<!DOCTYPE html>
<html lang="en">
<head>
<meta charset="utf-8">
<title>Maribel Quint – Business Card</title>
<link rel="stylesheet" href="https://fonts.googleapis.com/css2?family=Arvo:wght@400;700&display=swap">
<style>
  :root {
    --page-bg: #d9d4cf;
    --card-mauve: #6e5f5f;
    --lace-cream: #e6ddd4;
    --lace-mid: #a8999a;
    --text-cream: #ebe3da;
  }
  * { margin: 0; padding: 0; box-sizing: border-box; }
  html, body {
    width: 1200px;
    height: 900px;
    overflow: hidden;
    background: var(--page-bg);
    font-family: "Arvo", serif;
  }
  .canvas {
    position: relative;
    width: 1200px;
    height: 900px;
  }
  .card {
    position: absolute;
    left: 290px;
    width: 620px;
    height: 354px;
    background: var(--card-mauve);
    box-shadow: 0 6px 18px rgba(0,0,0,0.18);
    overflow: hidden;
  }
  .card--front { top: 60px; }
  .card--back { top: 474px; }

  .lace-band {
    position: absolute;
    left: 0;
    width: 100%;
    height: 78px;
    background: linear-gradient(to bottom, var(--lace-mid), var(--lace-cream) 55%, var(--lace-mid));
    opacity: 0.85;
  }
  .lace-band--top { top: 24px; }
  .lace-band--bottom { top: 244px; }

  .rule {
    position: absolute;
    left: 0;
    width: 100%;
    height: 3px;
    background: var(--lace-cream);
  }
  .rule--upper { top: 104px; }
  .rule--lower { top: 238px; }

  .centre-panel {
    position: absolute;
    top: 107px;
    left: 0;
    width: 100%;
    height: 131px;
    display: flex;
    flex-direction: column;
    justify-content: center;
    color: var(--text-cream);
  }
  .identity {
    align-items: center;
    padding-left: 90px;
  }
  .identity__name {
    font-weight: 700;
    font-size: 44px;
    letter-spacing: 1px;
    line-height: 1.1;
  }
  .identity__role {
    font-weight: 400;
    font-size: 17px;
    letter-spacing: 0.5px;
    align-self: center;
    margin-left: 180px;
    margin-top: 4px;
  }
  .contact {
    align-items: center;
    font-size: 18px;
    line-height: 1.45;
    padding-left: 60px;
  }
  .contact p { text-align: center; }
</style>
</head>
<body>
<main class="canvas">
  <section class="card card--front" aria-label="Business card front">
    <div class="lace-band lace-band--top" role="img" aria-label="Cream lace border pattern"></div>
    <div class="rule rule--upper"></div>
    <div class="centre-panel identity">
      <h1 class="identity__name">Maribel Quint</h1>
      <p class="identity__role">Fashion Designer</p>
    </div>
    <div class="rule rule--lower"></div>
    <div class="lace-band lace-band--bottom" role="img" aria-label="Cream lace border pattern"></div>
  </section>

  <section class="card card--back" aria-label="Business card back">
    <div class="lace-band lace-band--top" role="img" aria-label="Cream lace border pattern"></div>
    <div class="rule rule--upper"></div>
    <div class="centre-panel contact">
      <p>phone: 04 0152 6847</p>
      <p>vorinebyquint@mailbrook.com</p>
      <p>www.friendsnet.com/VOrineByQuint</p>
    </div>
    <div class="rule rule--lower"></div>
    <div class="lace-band lace-band--bottom" role="img" aria-label="Cream lace border pattern"></div>
  </section>
</main>
</body>
</html>
```